Schriftdesign für Shop-Header Bild (Schmuckhandel) / Online-Marketing Material
Zielgruppe
Wir verkaufen Schmuck im Onlineshop mit Herz
Aufgabenstellung
Wir benötigen den vorgegebenen Text in schöner Form, Farbe und Größe harmonisch eingefügt, in unserem Bild.
Folgender Text soll sich schick ins Bild einfügen oder in 3-D vielleicht in Schriftfarbe gold hervorheben:
Mit ganzem Herzen für Sie da!
Ihr Online -Juwelier mit Herz
Siehe auch unser altes Bild mit Text, im Shop, wie es nicht aussehen sollte: www.lindenglanzhof.de

```html
<!DOCTYPE html>
<html lang="de">
<head>
<meta charset="utf-8">
<title>Lindenglanzhof – Schmuck-Shop</title>
<link href="https://fonts.googleapis.com/css2?family=Lato:wght@400;700&family=Quicksand:wght@500&family=Great+Vibes&family=Handlee&display=swap" rel="stylesheet">
<style>
  :root{
    --red:#d0121b;
    --ink:#222;
    --grey:#6e6e6e;
    --nav:#6b6769;
    --field:#efefef;
    --brown:#5a2a10;
    --seal:#ebe7e1;
  }
  *{box-sizing:border-box;margin:0;padding:0}
  html,body{width:1200px;height:855px;overflow:hidden;background:#fff}
  body{position:relative;font-family:"Lato",sans-serif;color:var(--ink)}
  .abs{position:absolute}

  .brand{left:232px;top:36px;font-family:"Lato",sans-serif;font-weight:700;font-size:19px;color:var(--red);display:flex;align-items:center;gap:7px}
  .brand-dot{width:12px;height:12px;border-radius:50%;background:var(--red)}

  .toplinks{right:230px;top:7px;display:flex;gap:15px;font-size:9.5px}
  .toplinks a{color:var(--ink);text-decoration:none}
  .toplinks a.current{color:var(--red)}

  .search-label{left:421px;top:25px;font-size:12.5px;display:flex;align-items:center;gap:7px}
  .caret{width:0;height:0;border-left:4.5px solid transparent;border-right:4.5px solid transparent;border-top:5px solid var(--red);margin-top:3px}
  .search{left:421px;top:47px;width:320px;height:30px;background:var(--field);display:flex;align-items:center;justify-content:space-between;padding:0 14px 0 19px;font-size:10.5px;color:#888}
  .cart{left:783px;top:47px;width:187px;height:31px;background:var(--field);display:flex;align-items:center;justify-content:space-between;padding:0 16px 0 19px;font-size:10.5px;color:#e07070}

  .nav{left:0;top:104px;width:1200px;height:33px;background:var(--nav)}
  .nav-notch{left:250px;top:136px}
  .nav ul{position:absolute;left:324px;top:0;height:33px;display:flex;align-items:center;gap:29px;list-style:none;font-family:"Quicksand",sans-serif;font-size:13px;color:#fff;letter-spacing:.2px}

  .hero{left:0;top:137px;width:1200px;height:298px;
    background:
      radial-gradient(ellipse 110px 120px at 890px 140px,#e8c37a 0%,#d9a853 45%,rgba(217,168,83,0) 100%),
      linear-gradient(160deg,#f1efec 0%,#e6e2de 30%,#f4eee7 55%,#e2c8a8 80%,#f0e6dc 100%)}
  .hero-fade{left:0;top:425px;width:1200px;height:26px;background:linear-gradient(#e8e4e2,rgba(255,255,255,0))}
  .headline{left:182px;top:212px;width:550px;font-family:"Great Vibes",cursive;font-size:49px;line-height:58px;color:var(--brown);text-align:center}

  .seal{left:738px;top:461px;width:110px;height:66px;border-radius:8px;background:var(--seal)}
  .dots{left:727px;width:243px;height:4px;background-image:radial-gradient(circle,#d8d8d8 1.6px,transparent 2px);background-size:8.5px 4px}
  .perks{left:729px;top:554px;list-style:none}
  .perks li{display:flex;align-items:center;gap:7px;height:30px;font-size:13px;color:var(--red)}

  .store-line{left:230px;top:535px;font-size:14px;color:var(--grey)}
  .store-line small{font-size:12px}
  .banner{left:230px;top:569px;width:466px;height:156px;box-shadow:0 1px 4px rgba(0,0,0,.35);
    background:linear-gradient(90deg,#2a2a2a 0%,#3a3a3a 52%,#e0692a 64%,#f4b33c 72%,#6a6a6a 85%,#4d4d4d 100%);overflow:hidden}
  .banner-name{position:absolute;left:12px;top:12px;font-family:"Lato",sans-serif;font-size:36px;color:#c9a24a;letter-spacing:1px}
  .banner-card{position:absolute;left:2px;top:82px;width:175px;height:72px;background:#fff}
  .slider{position:absolute;right:20px;bottom:10px;display:flex;gap:6px}

  .welcome{left:230px;top:772px;font-family:"Handlee",cursive;font-size:20px;font-weight:400;color:var(--grey)}
  .welcome span{color:var(--red)}
  .tagline{left:230px;top:817px;font-size:15px;font-weight:700;color:var(--grey)}
</style>
</head>
<body>

<div class="abs brand"><span class="brand-dot"></span>Lindenglanzhof</div>

<nav class="abs toplinks">
  <a class="current" href="#">Startseite</a><a href="#">Anmelden</a><a href="#">Mein Konto</a><a href="#">Newsletter abonnieren</a><a href="#">Kontakt</a>
</nav>

<div class="abs search-label">Nach welchem Artikel suchen Sie? <span class="caret"></span></div>
<div class="abs search">Suchen nach
  <svg width="22" height="20" viewBox="0 0 22 20"><path d="M11 19 C4 13 1 10 1 6 A5 5 0 0 1 11 4 A5 5 0 0 1 21 6 C21 10 18 13 11 19Z" fill="var(--red)"/><circle cx="10.5" cy="8.5" r="2.6" fill="none" stroke="#fff" stroke-width="1.4"/><path d="M12.5 10.5l2 2" stroke="#fff" stroke-width="1.4"/></svg>
</div>
<div class="abs cart">Ihr Warenkorb ist leer.
  <svg width="16" height="19" viewBox="0 0 16 19"><path d="M5 6V4a3 3 0 0 1 6 0v2" fill="none" stroke="var(--red)" stroke-width="1.5"/><rect x="0" y="5" width="16" height="14" rx="1" fill="var(--red)"/><path d="M8 15c-2.5-2-3.5-3-3.5-4.3a1.7 1.7 0 0 1 3.5-.4 1.7 1.7 0 0 1 3.5.4C11.5 12 10.5 13 8 15Z" fill="#fff"/></svg>
</div>

<div class="abs nav">
  <ul><li>KREUZ-ANHÄNGER</li><li>ANHÄNGER/VERSCH.</li><li>FOTO-MEDAILLONS</li><li>OHRSCHMUCK</li><li>ACCESSOIRES</li></ul>
</div>
<svg class="abs nav-notch" width="64" height="16" viewBox="0 0 64 16"><path d="M0 0H64L32 16Z" fill="var(--nav)"/></svg>

<div class="abs hero" role="img" aria-label="Goldener Herzanhänger an feiner Kette auf cremefarbenem Seidenstoff"></div>
<div class="abs headline">Mit ganzem Herzen für Sie da!<br>Ihr Online -Juwelier mit Herz</div>
<div class="abs hero-fade"></div>

<div class="abs seal" role="img" aria-label="Platz für Käufersiegel"></div>

<div class="abs dots" style="top:534px"></div>
<ul class="abs perks">
  <li><svg width="26" height="22" viewBox="0 0 26 22"><path d="M13 21C5 15 1 11 1 6.5A5.5 5.5 0 0 1 13 4.5 5.5 5.5 0 0 1 25 6.5C25 11 21 15 13 21Z" fill="#f7b9be" stroke="var(--red)" stroke-width="1.2"/></svg>Versand innerhalb von 24 Stunden</li>
  <li><svg width="26" height="22" viewBox="0 0 26 22"><path d="M13 21C5 15 1 11 1 6.5A5.5 5.5 0 0 1 13 4.5 5.5 5.5 0 0 1 25 6.5C25 11 21 15 13 21Z" fill="#f7b9be" stroke="var(--red)" stroke-width="1.2"/></svg>schneller, persönlicher Service</li>
  <li><svg width="26" height="22" viewBox="0 0 26 22"><path d="M13 21C5 15 1 11 1 6.5A5.5 5.5 0 0 1 13 4.5 5.5 5.5 0 0 1 25 6.5C25 11 21 15 13 21Z" fill="#f7b9be" stroke="var(--red)" stroke-width="1.2"/></svg>Kundenzufriedenheit an erster Stelle</li>
  <li><svg width="26" height="22" viewBox="0 0 26 22"><path d="M13 21C5 15 1 11 1 6.5A5.5 5.5 0 0 1 13 4.5 5.5 5.5 0 0 1 25 6.5C25 11 21 15 13 21Z" fill="#f7b9be" stroke="var(--red)" stroke-width="1.2"/></svg>sichere Zahlungsmethoden</li>
</ul>
<div class="abs dots" style="top:684px"></div>

<div class="abs store-line">Besuchen Sie auch unseren AURIVANT-Schmuck Store: <small>hier</small></div>
<div class="abs banner" role="img" aria-label="Goldschmiedewerkstatt mit Flamme und Schmelztiegel">
  <div class="banner-name">AURIVANT</div>
  <div class="banner-card"></div>
  <div class="slider">
    <svg width="10" height="9" viewBox="0 0 26 22"><path d="M13 21C5 15 1 11 1 6.5A5.5 5.5 0 0 1 13 4.5 5.5 5.5 0 0 1 25 6.5C25 11 21 15 13 21Z" fill="#fff"/></svg>
    <svg width="10" height="9" viewBox="0 0 26 22"><path d="M13 21C5 15 1 11 1 6.5A5.5 5.5 0 0 1 13 4.5 5.5 5.5 0 0 1 25 6.5C25 11 21 15 13 21Z" fill="#fff"/></svg>
    <svg width="10" height="9" viewBox="0 0 26 22"><path d="M13 21C5 15 1 11 1 6.5A5.5 5.5 0 0 1 13 4.5 5.5 5.5 0 0 1 25 6.5C25 11 21 15 13 21Z" fill="var(--red)"/></svg>
    <svg width="10" height="9" viewBox="0 0 26 22"><path d="M13 21C5 15 1 11 1 6.5A5.5 5.5 0 0 1 13 4.5 5.5 5.5 0 0 1 25 6.5C25 11 21 15 13 21Z" fill="#fff"/></svg>
    <svg width="10" height="9" viewBox="0 0 26 22"><path d="M13 21C5 15 1 11 1 6.5A5.5 5.5 0 0 1 13 4.5 5.5 5.5 0 0 1 25 6.5C25 11 21 15 13 21Z" fill="#fff"/></svg>
    <svg width="10" height="9" viewBox="0 0 26 22"><path d="M13 21C5 15 1 11 1 6.5A5.5 5.5 0 0 1 13 4.5 5.5 5.5 0 0 1 25 6.5C25 11 21 15 13 21Z" fill="#fff"/></svg>
  </div>
</div>

<h1 class="abs welcome">Herzlich Willkommen im <span>Lindenglanzhof.de</span> Schmuck-Shop</h1>
<p class="abs tagline">Ihr Online-Juwelier mit Herz</p>

</body>
</html>
```